Tarvel Plumbing Solutions

This is for my new plumbing company, I have attached an example of what I’m going for but want it to look better.

Target Market(s)

Home owners, real estate, etc.

Industry/Entity Type

Plumbing

Font styles to use
Other font styles liked:
• As per my logo and other examples uploaded

Colors

Designer to choose colors to be used in the design.

Requirements
Must have
• Must include my logo provided and similar to my flyer I have attached but better

```html
<!DOCTYPE html>
<html lang="en">
<head>
<meta charset="utf-8">
<title>Tarvel Plumbing Solutions – Flyer</title>
<link href="https://fonts.googleapis.com/css2?family=Oswald:wght@500;600;700&family=Montserrat:wght@500;600;700&display=swap" rel="stylesheet">
<style>
  :root {
    --navy: #0a2c8c;
    --deep: #061a5c;
    --royal: #0e52d8;
    --cyan: #16a6f2;
    --cyan-dark: #0b86d0;
    --white: #ffffff;
    --ink: #0b2470;
    --page: #e9ecef;
  }
  * { box-sizing: border-box; margin: 0; padding: 0; }
  html, body { width: 915px; height: 1200px; overflow: hidden; background: var(--page); }
  .flyer {
    position: relative;
    width: 915px;
    height: 1200px;
    overflow: hidden;
    background: radial-gradient(ellipse at 55% 62%, var(--royal) 0%, var(--navy) 45%, var(--deep) 100%);
    font-family: "Oswald", "Arial Narrow", sans-serif;
    color: var(--white);
  }
  .hero-photo { position: absolute; inset: 0 0 auto 0; width: 915px; height: 580px; }
  .brand {
    position: absolute; left: 56px; top: 52px;
    display: flex; align-items: center; gap: 18px;
  }
  .brand-dot { width: 26px; height: 26px; border-radius: 50%; background: var(--white); }
  .brand-name {
    font-weight: 600; font-size: 46px; line-height: 1; letter-spacing: 1px;
    text-transform: uppercase; color: var(--white);
  }
  .brand-name small { display: block; font-size: 22px; letter-spacing: 3px; margin-top: 6px; font-weight: 600; }
  .headline {
    position: absolute; left: 56px; top: 220px;
    font-weight: 700; font-size: 66px; line-height: 1.02; color: var(--white);
  }
  .job-photo {
    position: absolute; left: 558px; top: 300px;
    width: 340px; height: 340px; border-radius: 50%;
    border: 11px solid var(--white);
    background: radial-gradient(circle at 40% 35%, #b08a62 0%, #6f5a47 40%, #2a2a2e 100%);
  }
  .intro {
    position: absolute; left: 56px; top: 600px;
    font-weight: 500; font-size: 27px; line-height: 1.2;
  }
  .services-title {
    position: absolute; left: 48px; top: 672px;
    font-weight: 700; line-height: 1.05;
  }
  .services-title .line-cyan { display: block; font-size: 68px; color: var(--cyan); }
  .services-title .line-white { display: block; font-size: 80px; color: var(--white); }
  .offer {
    position: absolute; left: 705px; top: 730px; width: 200px; height: 150px;
  }
  .offer-text {
    position: absolute; left: 0; top: 0; width: 170px; text-align: center;
    padding-top: 6px; color: var(--white);
  }
  .offer-big { font-weight: 700; font-size: 72px; line-height: 1; }
  .offer-big sup { font-size: 32px; vertical-align: 28px; }
  .offer-off { font-size: 28px; font-weight: 700; margin-left: -6px; }
  .offer-note { font-weight: 500; font-size: 12.5px; line-height: 1.15; margin-top: 2px; }
  .service-card {
    position: absolute; left: 40px; top: 876px; width: 835px; height: 234px;
    background: linear-gradient(180deg, #ffffff 0%, #eef1f6 100%);
    border-radius: 26px;
    display: grid; grid-template-columns: 1.15fr 1fr; padding: 16px 40px 0 46px;
  }
  .service-list { list-style: none; }
  .service-list li {
    position: relative; padding-left: 34px;
    font-weight: 500; font-size: 30px; line-height: 1.17; color: var(--ink);
  }
  .service-list li::before {
    content: ""; position: absolute; left: 0; top: 15px;
    width: 11px; height: 11px; border-radius: 50%; background: var(--ink);
  }
  .service-list.right { padding-top: 24px; }
  .contact { position: absolute; left: 56px; top: 1124px; font-family: "Montserrat", Arial, sans-serif; }
  .contact-email { font-weight: 500; font-size: 22px; }
  .contact-social { display: flex; align-items: center; gap: 12px; margin-top: 8px; }
  .social-dot { width: 20px; height: 20px; border-radius: 50%; background: var(--white); }
  .contact-handle { font-weight: 700; font-size: 20px; color: var(--cyan); }
  .call { position: absolute; right: 48px; top: 1124px; font-family: "Montserrat", Arial, sans-serif; text-align: left; }
  .call-label { font-weight: 500; font-size: 19px; }
  .call-number { font-weight: 700; font-size: 34px; color: var(--cyan); letter-spacing: 1px; margin-top: 2px; }
</style>
</head>
<body>
<main class="flyer">
  <svg class="hero-photo" viewBox="0 0 915 580" role="img" aria-label="Blue-toned photo of plumbing pipes and fittings under a sink">
    <defs>
      <linearGradient id="heroTone" x1="0" y1="0" x2="1" y2="1">
        <stop offset="0" stop-color="#0a2f8f"/>
        <stop offset="0.55" stop-color="#0f4db8"/>
        <stop offset="1" stop-color="#1570d6"/>
      </linearGradient>
    </defs>
    <polygon points="0,0 915,0 915,470 0,575" fill="url(#heroTone)"/>
    <line x1="0" y1="575" x2="915" y2="470" stroke="#ffffff" stroke-width="7"/>
  </svg>

  <header class="brand">
    <span class="brand-dot"></span>
    <div class="brand-name">Tarvel<small>Plumbing Solutions</small></div>
  </header>

  <h1 class="headline">Best Plumbing<br>Service in Sydney!</h1>

  <div class="job-photo" role="img" aria-label="Photo of a plumber carrying a toolbox beside a kitchen sink cabinet"></div>

  <p class="intro">Your local reliable Sydney Plumber<br>Specialising in all aspects of</p>

  <h2 class="services-title">
    <span class="line-cyan">Plumbing, Drainage &amp;</span>
    <span class="line-white">Gas Maintenance</span>
  </h2>

  <div class="offer">
    <svg width="200" height="150" viewBox="0 0 200 150" aria-hidden="true">
      <polygon points="150,20 200,30 175,150 120,128" fill="var(--cyan-dark)"/>
      <polygon points="20,0 170,10 165,130 0,118" fill="var(--cyan)"/>
      <polygon points="140,130 165,130 148,142" fill="#ffffff"/>
    </svg>
    <div class="offer-text">
      <div class="offer-big">15<sup>%</sup><span class="offer-off">OFF</span></div>
      <div class="offer-note">Mention this flyer to receive<br>Discount</div>
    </div>
  </div>

  <section class="service-card">
    <ul class="service-list left">
      <li>Emergency Plumbing</li>
      <li>Plumbing Maintenance</li>
      <li>Drainage Maintenance</li>
      <li>Gas maintenance</li>
      <li>Hot Water Systems</li>
    </ul>
    <ul class="service-list right">
      <li>Leaking Fixtures</li>
      <li>Blocked Sewer</li>
      <li>Stormwater</li>
      <li>Camera &amp; Locating</li>
      <li>TMV Maintenance</li>
    </ul>
  </section>

  <footer>
    <div class="contact">
      <div class="contact-email">hello@tarvelplumbing.com.au</div>
      <div class="contact-social">
        <span class="social-dot"></span>
        <span class="contact-handle">@TarvelPlumbingSolutions</span>
      </div>
    </div>
    <div class="call">
      <div class="call-label">More information call us</div>
      <div class="call-number">0491 570 156</div>
    </div>
  </footer>
</main>
</body>
</html>
```